Bref créative
Menu Card design for a Restaurant/Cafe
Lindor Ridge Brew
We are an established tea producing company based in Malaysia, with an up and coming chain of F&B tea tasting outlets cum restaurant around the country. We are looking for a revamp to our current menu card, something that reflects the 80 yr old heritage behind our company's experience in the tea industry and at the same time not alienating the younger generation looking for a hip and funky cafe to simply hang out.
link to my company website: www.quovaleaf.com.my
seven links to blogs & online article about my cafe:
http://www.dailyherald-sample.com.my/life/weekend/lindor-ridge-brew-pelita-1.220941
http://www.tesmorablog.com/2012/events/food/healthy-food/lindor-ridge-brew-house-pelita
http://www.dovinamerk.com/2012/05/4035/
http://oriventoph.examplog.com/2011/12/lindor-ridge-brew-cafe-lorong-semira.html
http://pendrua.my/2012/04/12/lindor-ridge-brew-pelita/
http://www.socialpage-sample.com/LindorRidge
https://www.searchpoint-sample.com.my/search?q=lindor+ridge&tbm=isch&q2=lindor+ridge+pelita
Food
Your average retail consumer
We have a variety of teas and food that we serve at our outlet. We only require a revamp to the design of the menu. Our name and company logo will remain the same.
Drinks menu to be included
Food menu to be included
Parent Company Profile for reference
Cafe name/brand/logo to be included in menu design
Parent Group logo to be included at the bottom of menu or at the back
Brief with references
image 1
image 2
image 3
image 4
image 5
image 6
image 7
image 8

```html
<!DOCTYPE html>
<html lang="en">
<head>
<meta charset="utf-8">
<title>Lindor Ridge Brew — Drinks Menu</title>
<link rel="stylesheet" href="https://fonts.googleapis.com/css2?family=Lora:wght@400;500&family=Open+Sans:wght@400;600&family=Kaushan+Script&display=swap">
<style>
  :root {
    --backdrop: #e9e4dc;
    --photo-frame: #ffffff;
    --parchment: #efe2c6;
    --parchment-edge: #dcc7a0;
    --ink: #3a2a1c;
    --ink-soft: #4b3a2a;
    --leaf: #6fae3a;
    --leaf-dark: #4f8f26;
    --drink-warm: #7a4a2c;
    --drink-red: #a8242a;
    --hill-green: #5f8a3c;
    --hill-light: #a9c48a;
  }
  * { box-sizing: border-box; margin: 0; padding: 0; }
  html, body {
    width: 1200px; height: 850px; overflow: hidden;
    background: var(--backdrop);
  }
  .spread { position: relative; width: 1200px; height: 850px; }

  .feature-photo {
    position: absolute; left: 72px; top: 89px; width: 451px; height: 674px;
    background: var(--photo-frame); padding: 12px;
    box-shadow: 0 4px 14px rgba(0,0,0,.25);
  }
  .feature-photo__image {
    width: 100%; height: 100%;
    background: linear-gradient(180deg, #3b1f1a 0%, var(--drink-red) 30%, var(--drink-warm) 55%, #c9b59b 80%, #e8e0d2 100%);
  }

  .menu-page {
    position: absolute; left: 672px; top: 84px; width: 456px; height: 684px;
    background: radial-gradient(ellipse at 50% 40%, #f6ecd6 0%, var(--parchment) 60%, var(--parchment-edge) 100%);
    box-shadow: 0 4px 14px rgba(0,0,0,.25);
    overflow: hidden;
    color: var(--ink);
  }
  .menu-page__landscape {
    position: absolute; left: 0; right: 0; bottom: 0; height: 210px;
    background: linear-gradient(180deg, rgba(169,196,138,0) 0%, var(--hill-light) 35%, var(--hill-green) 75%, #4a7030 100%);
  }

  .menu-title {
    position: absolute; left: 96px; top: 66px; width: 104px; height: 44px;
    background: var(--leaf); border-radius: 6px;
    display: flex; align-items: center; justify-content: center;
    font-family: "Kaushan Script", cursive; font-size: 26px; color: #ffffff;
  }

  .menu-section { position: absolute; left: 31px; width: 400px; }
  .menu-section--house { top: 150px; }
  .menu-section--local { top: 236px; }
  .menu-section--classic { top: 339px; }

  .menu-section__heading {
    font-family: "Lora", serif; font-weight: 400; font-size: 22px;
    text-align: center; margin-bottom: 14px; color: var(--ink);
  }
  .menu-list { list-style: none; font-family: "Open Sans", sans-serif; font-size: 10.5px; color: var(--ink-soft); }
  .menu-item {
    display: grid; grid-template-columns: 108px 67px 77px 65px 60px;
    line-height: 16px;
  }
  .menu-item__name { font-weight: 600; }
</style>
</head>
<body>
<main class="spread">
  <figure class="feature-photo">
    <div class="feature-photo__image" role="img" aria-label="Photo of an iced tea drink in a glass mug topped with cream and a blue straw, on a cafe table"></div>
  </figure>

  <section class="menu-page" aria-label="Drinks menu">
    <div class="menu-page__landscape" role="img" aria-label="Soft faded photo of green tea plantation hills"></div>

    <h1 class="menu-title">Drinks</h1>

    <div class="menu-section menu-section--house">
      <h2 class="menu-section__heading">House Specialty</h2>
      <ul class="menu-list">
        <li class="menu-item"><span class="menu-item__name">Cardamom Tea</span><span>(Cup) 6.00</span><span>(S) 10.00</span><span>(M) 18.00</span><span>(L) 23.00</span></li>
        <li class="menu-item"><span class="menu-item__name">Masala Tea</span><span>(Cup) 6.00</span><span>(S) 10.00</span><span>(M) 18.00</span><span>(L) 23.00</span></li>
      </ul>
    </div>

    <div class="menu-section menu-section--local">
      <h2 class="menu-section__heading">Local Speciality</h2>
      <ul class="menu-list">
        <li class="menu-item"><span></span><span class="menu-item__name">Teh Tarik</span><span>(Cup) 4.50</span></li>
        <li class="menu-item"><span></span><span class="menu-item__name">Triple Pleasure</span><span>(Cup) 9.00</span></li>
        <li class="menu-item"><span></span><span class="menu-item__name">Milky Lava</span><span>(Cup) 9.00</span></li>
      </ul>
    </div>

    <div class="menu-section menu-section--classic">
      <h2 class="menu-section__heading">Classic Tea</h2>
      <ul class="menu-list">
        <li class="menu-item"><span></span><span class="menu-item__name">Premium Black Tea</span><span>(S) 8.00</span><span>(M) 16.00</span><span>(L) 19.00</span></li>
        <li class="menu-item"><span></span><span class="menu-item__name">Breakfast Tea</span><span>(S) 8.00</span><span>(M) 16.00</span><span>(L) 19.00</span></li>
        <li class="menu-item"><span></span><span class="menu-item__name">Afternoon Tea</span><span>(S) 8.00</span><span>(M) 16.00</span><span>(L) 19.00</span></li>
      </ul>
    </div>
  </section>
</main>
</body>
</html>
```